VELOTRA Brisbane Tiling Service

My name is Milos Vrenbek i need a business card for a new company. We are wall and floor tilers based in Brisbane, our company is Velotra Brisbane Tiling Service.
We would like a logo from our website used on our cards. Our website is www.velotra-tiles.com.au

I would like my Facebook and Twitter accounts on my card.

Business

Colors
0692cd
3176b5
33a6d7
85cae6

```html
<!DOCTYPE html>
<html lang="en">
<head>
<meta charset="utf-8">
<title>Velotra Brisbane Tiling Service – Business Card</title>
<link rel="stylesheet" href="https://fonts.googleapis.com/css2?family=Jost:wght@400&family=Questrial&display=swap">
<style>
  :root {
    --page-bg: #e9e6e1;
    --card-bg: #fbfbf9;
    --brand-blue: #1f86c9;
    --brand-text: #2a6fa8;
    --ink: #1c1c1c;
    --rule: #9a9a9a;
    --teal: #4fc0a6;
    --orange: #f2a23a;
    --red: #e5543f;
    --blue: #2e8fcb;
    --purple: #85509f;
    --icon-blue: #3a7fb8;
    --icon-purple: #9a56b0;
    --icon-green: #3aa55b;
    --icon-red: #e04a3a;
    --icon-yellow: #f0b52c;
    --icon-grey: #555;
  }
  html, body {
    margin: 0;
    width: 1200px;
    height: 1000px;
    overflow: hidden;
    background: var(--page-bg);
  }
  .card {
    position: absolute;
    left: 100px;
    top: 210px;
    width: 1000px;
    height: 580px;
    background: var(--card-bg);
    box-shadow: 0 6px 24px rgba(0,0,0,0.12);
    overflow: hidden;
  }
  .card-art {
    position: absolute;
    inset: 0;
  }
  .brand {
    position: absolute;
    left: 70px;
    top: 215px;
    display: flex;
    align-items: flex-start;
    gap: 28px;
  }
  .brand-square {
    width: 140px;
    height: 140px;
    background: var(--brand-blue);
  }
  .brand-name {
    font-family: "Jost", sans-serif;
    font-weight: 400;
    font-size: 36px;
    line-height: 38px;
    letter-spacing: 1px;
    color: var(--brand-text);
    text-transform: uppercase;
    margin: 0;
  }
  .contact {
    position: absolute;
    right: 40px;
    font-family: "Questrial", sans-serif;
    font-size: 21px;
    color: var(--ink);
    text-transform: uppercase;
    text-align: right;
    white-space: nowrap;
    letter-spacing: 0.5px;
  }
  .contact-name { font-size: 26px; letter-spacing: 1px; }
</style>
</head>
<body>
  <div class="card">
    <svg class="card-art" width="1000" height="580" viewBox="0 0 1000 580">
      <!-- top stripe band -->
      <g class="band-top">
        <polygon points="0,0 600,0 594,8 0,8" fill="var(--teal)"/>
        <polygon points="0,8 594,8 588,16 0,16" fill="var(--orange)"/>
        <polygon points="0,16 588,16 582,24 0,24" fill="var(--red)"/>
        <polygon points="0,24 582,24 576,32 0,32" fill="var(--blue)"/>
        <polygon points="0,32 576,32 570,40 0,40" fill="var(--purple)"/>
      </g>
      <!-- bottom stripe band -->
      <g class="band-bottom">
        <polygon points="500,540 1000,540 1000,548 494,548" fill="var(--purple)"/>
        <polygon points="494,548 1000,548 1000,556 488,556" fill="var(--blue)"/>
        <polygon points="488,556 1000,556 1000,564 482,564" fill="var(--red)"/>
        <polygon points="482,564 1000,564 1000,572 476,572" fill="var(--orange)"/>
        <polygon points="476,572 1000,572 1000,580 470,580" fill="var(--teal)"/>
      </g>
      <!-- divider -->
      <line x1="570" y1="40" x2="500" y2="540" stroke="var(--rule)" stroke-width="3"/>
      <!-- separators -->
      <g class="separators" stroke="var(--rule)" stroke-width="2">
        <line x1="557" y1="135" x2="960" y2="135"/>
        <line x1="545" y1="215" x2="960" y2="215"/>
        <line x1="535" y1="293" x2="960" y2="293"/>
        <line x1="528" y1="338" x2="960" y2="338"/>
        <line x1="522" y1="383" x2="960" y2="383"/>
        <line x1="516" y1="428" x2="960" y2="428"/>
      </g>
      <!-- icons -->
      <g class="icon-person" fill="var(--icon-blue)">
        <circle cx="585" cy="64" r="6"/>
        <path d="M574 84 q11 -16 22 0 z"/>
      </g>
      <g class="icon-chair" fill="none" stroke="var(--icon-purple)" stroke-width="2.5">
        <rect x="577" y="96" width="14" height="9" fill="var(--icon-purple)"/>
        <line x1="584" y1="105" x2="584" y2="114"/>
        <line x1="576" y1="116" x2="592" y2="116"/>
      </g>
      <path class="icon-phone" d="M572 143 q-4 8 4 16 q8 8 16 4 l-3 -5 q-5 2 -10 -3 q-5 -5 -3 -10 z" fill="var(--icon-green)"/>
      <g class="icon-pin">
        <path d="M564 222 a9 9 0 0 1 18 0 q0 8 -9 18 q-9 -10 -9 -18 z" fill="var(--icon-red)"/>
        <circle cx="573" cy="222" r="3.5" fill="#fff"/>
      </g>
      <g class="icon-mail">
        <rect x="552" y="303" width="22" height="15" fill="var(--icon-yellow)"/>
        <polyline points="552,303 563,312 574,303" fill="none" stroke="#fff" stroke-width="1.5"/>
      </g>
      <g class="icon-globe">
        <circle cx="555" cy="358" r="10" fill="var(--icon-grey)"/>
        <ellipse cx="555" cy="358" rx="4" ry="10" fill="none" stroke="#fff" stroke-width="1.2"/>
        <line x1="545" y1="358" x2="565" y2="358" stroke="#fff" stroke-width="1.2"/>
      </g>
      <rect class="icon-social" x="536" y="392" width="20" height="20" fill="var(--icon-blue)"/>
      <rect class="icon-social" x="529" y="435" width="20" height="20" fill="var(--blue)"/>
    </svg>

    <div class="brand">
      <div class="brand-square"></div>
      <p class="brand-name">Velotra<br>Brisbane<br>Tiling<br>Service</p>
    </div>

    <div class="contact contact-name" style="top:56px">Tarun Mehvali</div>
    <div class="contact" style="top:98px">CEO, Founder</div>
    <div class="contact" style="top:143px">+91 5550142786</div>
    <div class="contact" style="top:177px">+91 5550193364</div>
    <div class="contact" style="top:222px">Your address your address</div>
    <div class="contact" style="top:256px">Your address your address</div>
    <div class="contact" style="top:302px">youremail@email.com</div>
    <div class="contact" style="top:347px">www.website.com</div>
    <div class="contact" style="top:392px">FB/tileprobne</div>
    <div class="contact" style="top:437px">Twitter/@profile</div>
  </div>
</body>
</html>
```